Dietitian needs awesome business card

I need a contemporary design that's eye catching but professional.
My card is to given to doctors, specialists and patients alike.
I manage patients with chronic diseases
I have uploaded my logo and current business card, I would also like the other Registered Clinical Nutritionist logo incorporated into the design

Target Market(s)

Doctors, specialists and patients

Industry/Entity Type

Healthcare

Contact Information for Business Card

www.brindlecovenutrition.com.au
Ph: 0427 516 903
Fax: 6482 7315
email: marcus.k.wellfare@quorvamail.com
Space on the back of the card with: Appointment date, Appointment time and appointment location

Font styles to use
Serif

Colors
fbee3e
876aae
ffc214

Requirements
Must have
• My Logo
• Registered Clinical Nutritionist Logo
• My 4 locations - Fernhollow Medical Centre, North Kelby Health, Ashcourt Medical, Pinebrook Doctors Surgery
Nice to have
• I like the colours in my current business card

```html
<!DOCTYPE html>
<html lang="en">
<head>
<meta charset="utf-8">
<title>Brindle Cove Nutrition &amp; Dietetics – Business Card</title>
<link href="https://fonts.googleapis.com/css2?family=Fira+Sans:wght@300;400&display=swap" rel="stylesheet">
<style>
  :root {
    --backdrop: #8f8f8f;
    --card: #ffffff;
    --navy: #1f3a93;
    --blue-deep: #1a3d9c;
    --blue-bright: #1e74d8;
    --green: #7cc242;
    --text: #3d3d3d;
    --rule: #9a9a9a;
    --orange: #f47b20;
  }
  * { margin: 0; padding: 0; box-sizing: border-box; }
  html, body { width: 1105px; height: 1200px; overflow: hidden; }
  body {
    background: var(--backdrop);
    font-family: "Fira Sans", sans-serif;
    font-weight: 300;
    color: var(--text);
    position: relative;
  }
  .card {
    position: absolute;
    left: 182px;
    width: 746px;
    height: 424px;
    background: var(--card);
  }
  .card--front { top: 120px; }
  .card--back { top: 637px; }

  /* Front */
  .name-band {
    position: absolute;
    left: 0; top: 62px;
    width: 420px; height: 97px;
    background: linear-gradient(90deg, var(--blue-deep) 0%, var(--blue-bright) 100%);
    color: #fff;
    padding: 22px 0 0 46px;
  }
  .name-band__name { font-size: 25px; font-weight: 400; line-height: 1.2; }
  .name-band__role { font-size: 18px; font-weight: 400; margin-top: 4px; }
  .brand-mark {
    position: absolute;
    border-radius: 50%;
    background: #fff;
    border: 6px solid var(--green);
  }
  .card--front .brand-mark { left: 382px; top: 52px; width: 112px; height: 112px; }
  .brand-name {
    position: absolute;
    left: 506px; top: 78px;
    color: var(--navy);
    font-weight: 400;
    font-size: 25px;
    line-height: 1.2;
  }
  .contact {
    position: absolute;
    top: 322px;
    font-size: 21px;
    line-height: 28px;
  }
  .contact--left { left: 46px; }
  .contact--right { right: 46px; text-align: right; }
  .contact__row { display: flex; align-items: center; gap: 10px; }
  .contact--right .contact__row { justify-content: flex-end; }
  .icon { width: 19px; height: 19px; flex: none; }

  /* Back */
  .card--back .brand-mark { left: 48px; top: 34px; width: 82px; height: 82px; }
  .credential-badge {
    position: absolute;
    left: 518px; top: 39px;
    width: 176px; height: 84px;
    background: var(--orange);
    border-radius: 3px;
  }
  .note-line {
    position: absolute;
    left: 50px; width: 645px;
    border-top: 1px solid var(--rule);
  }
  .appointment {
    position: absolute;
    left: 50px; top: 274px;
    width: 645px;
    display: flex;
    align-items: baseline;
    color: var(--navy);
    font-size: 21px;
    font-weight: 400;
  }
  .appointment__fill {
    border-bottom: 2px dotted var(--navy);
    margin: 0 8px;
    height: 1px;
    align-self: flex-end;
    margin-bottom: 6px;
  }
  .appointment__fill--date { flex: 0 0 298px; }
  .appointment__fill--time { flex: 1; }
  .appointment__ampm { font-size: 16px; }
  .locations {
    position: absolute;
    top: 330px;
    list-style: none;
    font-size: 20px;
    line-height: 31px;
    color: var(--text);
  }
  .locations--left { left: 50px; }
  .locations--right { left: 425px; }
  .locations li { display: flex; align-items: center; gap: 10px; }
  .checkbox {
    width: 16px; height: 16px;
    border: 1.5px solid var(--navy);
    flex: none;
  }
</style>
</head>
<body>

<section class="card card--front">
  <div class="name-band">
    <div class="name-band__name">Marcus Wellfare</div>
    <div class="name-band__role">Nutritionist &amp; Chef</div>
  </div>
  <div class="brand-mark" aria-hidden="true"></div>
  <div class="brand-name">Brindle Cove<br>Nutrition &amp; Dietetics</div>

  <div class="contact contact--left">
    <div class="contact__row">
      <svg class="icon" viewBox="0 0 20 20" aria-hidden="true"><path fill="#1f3a93" d="M5 1.5l3 3.5-1.8 2.2c1 2.2 2.6 3.8 4.6 4.8L13 10.2l3.5 3-1.6 3.3C8.5 16.3 3.7 11.5 3.4 3z"/></svg>
      <span>0427 516 903</span>
    </div>
    <div class="contact__row">
      <svg class="icon" viewBox="0 0 20 20" aria-hidden="true"><rect x="5" y="2" width="10" height="6" fill="#1f3a93"/><rect x="1.5" y="7.5" width="17" height="8" rx="1.5" fill="#1f3a93"/><rect x="5" y="13" width="10" height="5" fill="#fff" stroke="#1f3a93" stroke-width="1.5"/></svg>
      <span>6482 7315</span>
    </div>
  </div>

  <div class="contact contact--right">
    <div class="contact__row">
      <span>marcus.k.wellfare@quorvamail.com</span>
      <svg class="icon" viewBox="0 0 20 20" aria-hidden="true"><rect x="1.5" y="4" width="17" height="12" fill="#1f3a93"/><path d="M2 4.5l8 6.5 8-6.5" fill="none" stroke="#fff" stroke-width="1.4"/></svg>
    </div>
    <div class="contact__row">
      <span>brindlecovenutrition.com.au</span>
      <svg class="icon" viewBox="0 0 20 20" aria-hidden="true"><circle cx="10" cy="10" r="8.5" fill="#1f3a93"/><path d="M1.5 10h17M10 1.5c-3.5 4-3.5 13 0 17M10 1.5c3.5 4 3.5 13 0 17" fill="none" stroke="#fff" stroke-width="1.1"/></svg>
    </div>
  </div>
</section>

<section class="card card--back">
  <div class="brand-mark" aria-hidden="true"></div>
  <div class="credential-badge" role="img" aria-label="Registered Clinical Nutritionist credential badge"></div>

  <div class="note-line" style="top:167px"></div>
  <div class="note-line" style="top:207px"></div>
  <div class="note-line" style="top:247px"></div>

  <div class="appointment">
    <span>Date :</span>
    <span class="appointment__fill appointment__fill--date"></span>
    <span>Time :</span>
    <span class="appointment__fill appointment__fill--time"></span>
    <span class="appointment__ampm">AM/PM</span>
  </div>

  <ul class="locations locations--left">
    <li><span class="checkbox"></span>Fernhollow Medical Centre</li>
    <li><span class="checkbox"></span>North Kelby Health</li>
  </ul>
  <ul class="locations locations--right">
    <li><span class="checkbox"></span>Pinebrook Doctors Surgery</li>
    <li><span class="checkbox"></span>Ashcourt Medical</li>
  </ul>
</section>

</body>
</html>
```